Tallyleaf Web Design

Create Website Design for Tallyleaf. Tallyleaf is online application for collaboration team work system (task list management). More concept design for this project please find attach file ("tallyleaf website concept.pdf") . But my concept is just describe minimal features not bind design

For tallyleaf logo, i had already attach files. But i had not decided what color i chose, so it's okay if you suggest logo color for your suitable website design.
Updates

Dear All Designer,

I like brisk carousel (http://quorvanlabs.example/brisk-carousel/),
may be your concept design can adjust with this concept.
but don't worry about script for brisk carousel, my team will be handle
You just make website design to suitable with brisk carousel

but if you had own website design concept are welcome

thanks

Target Market(s)

Business Company

Industry/Entity Type

Management

```html
<!DOCTYPE html>
<html lang="en">
<head>
<meta charset="utf-8">
<title>Tallyleaf – Online Collaboration Team Work</title>
<link href="https://fonts.googleapis.com/css2?family=Kreon:wght@400;700&family=Didact+Gothic&family=Open+Sans:wght@400;600;700&display=swap" rel="stylesheet">
<style>
:root{
  --green:#6aa72c;
  --lime:#c8e03a;
  --teal:#2b8c8f;
  --orange:#f07d1a;
  --dark:#2a2a2a;
  --beige:#efebe1;
  --text:#3f3f3f;
  --muted:#6a6a6a;
  --blue:#2f7fb8;
  --blue-light:#8ec3e6;
  --band:#5a9bd0;
  --footer:#2e72ad;
  --white:#ffffff;
}
*{margin:0;padding:0;box-sizing:border-box}
html,body{width:1200px;height:2182px;overflow:hidden}
body{position:relative;background:var(--white);font-family:"Open Sans",Arial,sans-serif;color:var(--text)}
.abs{position:absolute}

/* header */
.site-header{left:0;top:0;width:1200px;height:120px;background:var(--white)}
.brand{left:142px;top:30px;display:flex;align-items:center;gap:12px;font-family:"Open Sans",Arial,sans-serif;font-weight:700;font-size:52px;color:var(--green);letter-spacing:-1px}
.brand-dot{width:30px;height:30px;border-radius:50%;background:var(--green)}
.login{left:964px;top:15px;width:92px;height:36px;background:#1e8a6a;border-radius:4px;color:var(--white);font-weight:700;font-size:15px;display:flex;align-items:center;justify-content:center;gap:8px;box-shadow:0 2px 0 #0f5a43}
.main-nav{left:473px;top:80px;display:flex;height:38px;border-top:1px solid #ddd}
.main-nav a{display:flex;align-items:center;padding:0 16px;font-size:16px;color:#333;text-decoration:none;border-left:1px solid #ddd;height:38px}
.main-nav a:last-child{border-right:1px solid #ddd}
.main-nav a.active{color:var(--orange);font-weight:600}

/* hero */
.hero{left:0;top:120px;width:1200px;height:425px;background:linear-gradient(#2d2d2d,#1f1f1f)}
.hero-title{left:0;top:144px;width:1200px;text-align:center;font-family:"Kreon",Georgia,serif;font-weight:400;font-size:35px;color:var(--white)}
.hero-title em{font-style:normal;font-weight:700;color:var(--lime)}
.app-window{border:1px solid #999;border-radius:4px 4px 0 0;background:linear-gradient(#e6e9ee,#c9ced6)}

/* features */
.features{left:0;top:545px;width:1200px;height:1100px;background:var(--beige)}
.feature-title{font-family:"Didact Gothic",Arial,sans-serif;font-weight:400;font-size:46px;line-height:1}
.feature-text{width:490px;font-size:15.5px;line-height:22px;color:var(--text)}
.t-green{color:var(--green)}
.t-teal{color:var(--teal)}
.t-orange{color:var(--orange)}

/* bottom */
.info-heading{font-size:24px;font-weight:700;color:#111;line-height:1}
.info-heading span{display:block;font-weight:400;font-size:24px;color:#555}
.info-text{font-size:14px;line-height:22px;color:var(--muted)}
.learn-more{font-size:12px;font-weight:700;color:var(--blue);text-decoration:none}
.quote-mark{font-family:"Kreon",serif;font-size:90px;color:#ddd;line-height:1}
.quick-contact{left:778px;top:1673px;width:279px;height:310px;background:var(--blue-light);border-radius:4px;box-shadow:0 2px 4px rgba(0,0,0,.2)}
.quick-contact h3{padding:10px 10px 6px;font-size:20px;color:var(--white);font-weight:700}
.qc-field{position:absolute;left:17px;width:239px;height:28px;background:#dcebf5;border:1px solid #b9d3e6;font-size:13px;color:#333;padding:6px 8px}
.send-btn{left:19px;top:265px;width:56px;height:28px;background:linear-gradient(#f9b31f,#ef8a06);border-radius:3px;color:var(--white);font-weight:700;font-size:14px;display:flex;align-items:center;justify-content:center}

/* newsletter & footer */
.newsletter{left:0;top:2036px;width:1200px;height:56px;background:var(--band)}
.social{width:30px;height:30px;border-radius:50%;background:#3b6fa8;top:2049px}
.join{left:505px;top:2040px;width:260px;text-align:right;white-space:nowrap;color:var(--white);font-family:"Didact Gothic",sans-serif;font-size:21px;line-height:22px}
.join strong{display:block;font-family:"Open Sans",sans-serif;font-size:18px;line-height:22px;font-weight:700}
.news-note{left:775px;top:2039px;font-size:12px;font-weight:700;color:var(--white)}
.news-input{left:775px;top:2058px;width:224px;height:24px;background:var(--white);font-size:12px;color:#555;padding:4px 8px}
.news-btn{left:1002px;top:2058px;width:58px;height:24px;background:#1d5e93;color:var(--white);font-size:11px;font-weight:700;display:flex;align-items:center;justify-content:center}
.site-footer{left:0;top:2092px;width:1200px;height:90px;background:var(--footer);color:var(--white)}
.footer-nav{left:222px;top:2114px;display:flex;gap:38px;font-size:14px;align-items:center}
.footer-legal{left:140px;top:2158px;font-size:12px}
.copyright{right:140px;top:2158px;font-size:12px}
</style>
</head>
<body>

<header class="abs site-header">
  <div class="abs brand"><span class="brand-dot"></span>tallyleaf</div>
  <div class="abs login">
    <svg width="12" height="14" viewBox="0 0 12 14"><circle cx="6" cy="4" r="3.5" fill="#fff"/><path d="M0 14c0-4 3-6 6-6s6 2 6 6z" fill="#fff"/></svg>LOGIN
  </div>
  <nav class="abs main-nav">
    <a class="active">Home</a><a>About Us</a><a>Services</a><a>Products</a><a>Testimonials</a><a>Contact Us</a>
  </nav>
</header>

<section class="abs hero">
</section>
<h1 class="abs hero-title">Customize <em>Online Collaboration</em> Team Work</h1>
<div class="abs app-window" style="left:195px;top:310px;width:130px;height:235px;opacity:.75"></div>
<div class="abs app-window" style="left:875px;top:325px;width:130px;height:220px;opacity:.75"></div>
<div class="abs app-window" role="img" aria-label="Screenshot of the Tallyleaf transaction list application window" style="left:291px;top:222px;width:618px;height:323px;background:linear-gradient(#f1f2f4 0%,#e2e5ea 30%,#fdfdfd 31%,#fdfdfd 72%,#d5d9df 73%,#c6cbd2 100%)"></div>

<section class="abs features"></section>

<svg class="abs" style="left:154px;top:567px" width="310" height="310" viewBox="0 0 310 310">
  <circle cx="155" cy="155" r="153" fill="none" stroke="#8fc45a" stroke-width="1"/>
  <circle cx="155" cy="155" r="140" fill="none" stroke="#8fc45a" stroke-width="1"/>
  <circle cx="155" cy="155" r="125" fill="none" stroke="#8fc45a" stroke-width="1.5"/>
  <circle cx="155" cy="155" r="112" fill="#fff"/>
</svg>
<div class="abs" role="img" aria-label="Hand holding a tablet showing the application" style="left:220px;top:650px;width:180px;height:145px;border-radius:50%;background:radial-gradient(#cfd8e0,#9aa8b4)"></div>
<h2 class="abs feature-title t-green" style="left:513px;top:645px">Customize Application</h2>
<p class="abs feature-text" style="left:513px;top:698px">Lorem ipsum dolor sit amet, consectetur adipisicing elit, sed do eiusmod tempor incididunt ut labore et dolore. magna aliqua. Ut enim ad minim veniam, quis nostrud exercitation ullamco laboris nisi ut aliquip ex ea commodo consequat. Duis aute irure dolor in reprehenderit in voluptate velit esse cillum.</p>

<svg class="abs" style="left:727px;top:912px" width="310" height="310" viewBox="0 0 310 310">
  <circle cx="155" cy="155" r="153" fill="none" stroke="#6bbfc0" stroke-width="1"/>
  <circle cx="155" cy="155" r="140" fill="none" stroke="#6bbfc0" stroke-width="1"/>
  <circle cx="155" cy="155" r="125" fill="none" stroke="#2b8c8f" stroke-width="1.5"/>
  <circle cx="155" cy="155" r="112" fill="#fff"/>
</svg>
<div class="abs" role="img" aria-label="Tablet, phone and laptop showing synchronized data" style="left:800px;top:1005px;width:165px;height:125px;border-radius:10px;background:linear-gradient(#5a5f66,#2c3036)"></div>
<h2 class="abs feature-title t-teal" style="left:198px;top:998px">Synchronize All Device</h2>
<p class="abs feature-text" style="left:198px;top:1052px">Lorem ipsum dolor sit amet, consectetur adipisicing elit, sed do eiusmod tempor incididunt ut labore et dolore. magna aliqua. Ut enim ad minim veniam, quis nostrud exercitation ullamco laboris nisi ut aliquip ex ea commodo consequat. Duis aute irure dolor in reprehenderit in voluptate velit esse cillum.</p>

<svg class="abs" style="left:187px;top:1267px" width="310" height="310" viewBox="0 0 310 310">
  <circle cx="155" cy="155" r="153" fill="none" stroke="#f5a862" stroke-width="1"/>
  <circle cx="155" cy="155" r="140" fill="none" stroke="#f5a862" stroke-width="1"/>
  <circle cx="155" cy="155" r="125" fill="none" stroke="#f07d1a" stroke-width="1.5"/>
  <circle cx="155" cy="155" r="112" fill="#fff"/>
</svg>
<div class="abs" role="img" aria-label="Tablet displaying report charts with a pen" style="left:225px;top:1360px;width:175px;height:125px;border-radius:14px;background:linear-gradient(135deg,#e8eef3,#9fb6c8)"></div>
<h2 class="abs feature-title t-orange" style="left:513px;top:1352px">Report</h2>
<p class="abs feature-text" style="left:513px;top:1406px">Lorem ipsum dolor sit amet, consectetur adipisicing elit, sed do eiusmod tempor incididunt ut labore et dolore. magna aliqua. Ut enim ad minim veniam, quis nostrud exercitation ullamco laboris nisi ut aliquip ex ea commodo consequat. Duis aute irure dolor in reprehenderit in voluptate velit esse cillum.</p>

<section>
  <h3 class="abs info-heading" style="left:142px;top:1690px">Why<span>Tallyleaf</span></h3>
  <p class="abs info-text" style="left:140px;top:1752px;width:280px">Lorem ipsum dolor sit amet, consectetur adipisicing elit, sed do eiusmod tempor incididunt ut labore et dolore magna aliqua. Ut enim ad minim veniam, quis nostrud exercitation ullamco laboris nisi ut aliquip ex ea commodo consequat. Duis aute irure dolor in reprehenderit in voluptate velit esse cillum.</p>
  <a class="abs learn-more" style="left:140px;top:1935px">LEARN MORE</a>

  <h3 class="abs info-heading" style="left:449px;top:1694px;font-size:22px">Customer<span style="font-size:22px">Say</span></h3>
  <div class="abs quote-mark" style="left:448px;top:1750px">&ldquo;</div>
  <p class="abs info-text" style="left:506px;top:1752px;width:245px">Lorem ipsum dolor sit amet, consectetur adipisicing elit, sed do eiusmod tempor incididunt ut labore et dolore magna aliqua. Ut enim ad minim veniam, quis nostrud exercitation ullamco laboris nisi ut aliquip ex ea commodo.</p>
  <p class="abs" style="left:503px;top:1922px;font-size:14px;color:#333">John Doe, Some Business</p>

  <form class="abs quick-contact">
    <h3>Quick Contact</h3>
    <div class="qc-field" style="top:44px">Enter your name</div>
    <div class="qc-field" style="top:80px">Enter your email</div>
    <div class="qc-field" style="top:116px;height:76px">Enter a message</div>
    <div class="abs" style="left:19px;top:198px;font-size:11px;color:#333"><b>5000</b> characters left</div>
    <div class="abs" role="img" aria-label="Captcha image" style="left:19px;top:215px;width:104px;height:32px;background:linear-gradient(90deg,#f4f4f4,#d0d0d0)"></div>
    <div class="qc-field" style="top:220px;left:145px;width:112px"></div>
    <div class="abs send-btn">Submit</div>
  </form>
</section>

<div class="abs newsletter"></div>
<div class="abs social" style="left:140px"></div>
<div class="abs social" style="left:176px"></div>
<div class="abs join">JOIN US<strong>OUR NEWSLETTER</strong></div>
<div class="abs news-note">Services updates and special offers in your mailbox!</div>
<div class="abs news-input">Email Address</div>
<div class="abs news-btn">SIGN UP</div>

<footer class="abs site-footer"></footer>
<nav class="abs footer-nav" style="color:#fff">
  <span>Home</span><span>About Us</span><span>Products</span><span>Testimonials</span><span>Contact Us</span>
  <span style="display:flex;align-items:center;gap:8px">
    <svg width="18" height="18" viewBox="0 0 24 24"><path d="M6.6 10.8a15 15 0 0 0 6.6 6.6l2.2-2.2c.3-.3.7-.4 1-.2 1.1.4 2.3.6 3.6.6.6 0 1 .4 1 1V20c0 .6-.4 1-1 1C10.6 21 3 13.4 3 4c0-.6.4-1 1-1h3.5c.6 0 1 .4 1 1 0 1.3.2 2.5.6 3.6.1.3 0 .7-.2 1z" fill="#fff"/></svg>(555) 014-2290</span>
  <span style="display:flex;align-items:center;gap:8px">
    <svg width="18" height="14" viewBox="0 0 18 14"><rect x="0.5" y="0.5" width="17" height="13" fill="none" stroke="#fff"/><path d="M1 1l8 7 8-7" fill="none" stroke="#fff"/></svg>info@tallyleaf.com</span>
</nav>
<div class="abs footer-legal" style="color:#fff">Disclaimer &nbsp;|&nbsp; Terms &amp; Conditions &nbsp;|&nbsp; Privacy Policy &nbsp;|&nbsp; Site Map</div>
<div class="abs copyright" style="color:#fff">© 2013 Tallyleaf.</div>

</body>
</html>
```